New Dental Office Needs an Attractive and user friendly Website Designed

I need a website for a new dental office. The Name is Maplecrest Dentistry. I would like a Modern design with a user friendly interface and usability.
I would like a landing page, a page that lists the services we offer: Cosmetic Dentistry, Implants, Dental Hygiene, Emergency Services, Restorations, Dentures
Target Market(s)
Mid to upper class
Industry/Entity Type
Dentistry
Coding
Coded - Design and coding required
Number of Pages Required
1 page
Requirements
Must have
- Landing page that has a scheduling option, Procedures, operating hours, and contact us info
Nice to have
- Appealing design, Soft comforting colors. Easy to navigate page, Modern and professional.

```html
<!DOCTYPE html>
<html lang="en">
<head>
<meta charset="utf-8">
<title>Maplecrest Dentistry</title>
<link href="https://fonts.googleapis.com/css2?family=Poppins:wght@300;400;500;600;700&display=swap" rel="stylesheet">
<style>
:root{
  --blue:#3e5dd8;
  --blue-dark:#2f4cc4;
  --navy:#0e1a45;
  --ink:#1c1d2b;
  --text:#4a4d5e;
  --muted:#8a8ea3;
  --hero-bg:#dee4fb;
  --soft:#eef1fc;
  --card-bg:#eef1fc;
  --white:#ffffff;
  --line:#d8dbe6;
}
*{margin:0;padding:0;box-sizing:border-box}
html,body{width:1200px;height:3841px;overflow:hidden}
body{font-family:'Poppins',sans-serif;color:var(--ink);background:var(--white);position:relative}
.abs{position:absolute}
a{color:inherit;text-decoration:none}
.btn{position:absolute;display:flex;align-items:center;justify-content:center;background:var(--blue);color:var(--white);font-size:14px;font-weight:500;border-radius:5px}
.eyebrow{color:var(--blue);font-size:14px;font-weight:400}
.section-title{font-size:33px;font-weight:600;color:var(--ink);line-height:1.2}
.center{left:0;width:1200px;text-align:center}
.lead{font-size:14.5px;color:var(--text);line-height:20px}

/* hero */
.hero{position:absolute;left:0;top:0;width:1200px;height:648px;background:var(--hero-bg);overflow:hidden}
.deco-ring{position:absolute;border:40px solid #c7cff6;border-radius:50%}
.logo{position:absolute;font-family:'Poppins',sans-serif;font-weight:600;font-size:24px;color:var(--ink);line-height:1}
.nav{position:absolute;top:33px;left:435px;display:flex;gap:36px;font-size:14px;color:var(--ink)}
.nav .active{color:var(--blue)}
.hero h1{position:absolute;left:161px;top:218px;font-size:50px;font-weight:600;line-height:62px;color:var(--ink)}
.hero h1 span{color:var(--blue)}
.hero p{position:absolute;left:161px;top:352px;width:450px;font-size:15.5px;line-height:18px;color:var(--text)}
.hero-photo{position:absolute;left:678px;top:104px;width:485px;height:596px;border-radius:30px 30px 0 0;background:linear-gradient(180deg,#c9d2f5 0%,#f3f5fc 60%,#e6e9f3 100%)}
.info-card{position:absolute;display:flex;align-items:center;gap:14px;border-radius:12px;box-shadow:0 10px 30px rgba(40,60,140,.15)}
.info-card .t1{font-size:13.5px;font-weight:600}
.info-card .t2{font-size:12px}

/* about */
.ph{position:absolute;border-radius:6px}
/* services */
.services{position:absolute;left:0;top:1257px;width:1200px;height:653px;background:var(--soft)}
.svc{position:absolute;top:1485px;width:261px;height:261px;background:var(--white);border:1px solid #e1e4ef;border-radius:4px;overflow:hidden}
.svc .icon{position:absolute;left:19px;top:18px;width:56px;height:56px;border-radius:50%;border:2px solid #bcc7f2;display:flex;align-items:center;justify-content:center}
.svc h3{position:absolute;left:26px;top:89px;font-size:17px;font-weight:600}
.svc p{position:absolute;left:26px;top:118px;width:200px;font-size:11px;line-height:16.5px;color:var(--muted)}
.svc .more{position:absolute;left:26px;top:181px;font-size:11px;color:var(--blue)}
.svc .thumb{position:absolute;right:0;bottom:0;width:122px;height:84px;border-radius:20px 0 0 0;background:linear-gradient(160deg,#ffffff 0%,#f1f1f4 45%,#e7a1a8 75%,#d46e7a 100%)}

/* team */
.member{position:absolute;top:2123px;width:200px;height:244px;border-radius:4px}
.member .tag{position:absolute;left:15px;right:15px;bottom:9px;height:67px;background:var(--white);border-radius:4px;text-align:center;padding-top:16px;box-shadow:0 6px 18px rgba(0,0,0,.08)}
.member .name{font-size:14.5px;font-weight:500}
.member .role{font-size:12px;color:var(--muted);margin-top:1px}

/* testimonials */
.review{position:absolute;top:2661px;width:253px;height:253px;background:var(--card-bg);padding:0 27px}
.review.faded{opacity:.45}
.review .stars{position:absolute;top:36px;left:27px;display:flex;gap:3px}
.review .quote{position:absolute;top:78px;left:27px;font-size:15px;font-weight:500;line-height:19px}
.review .body{position:absolute;top:128px;left:27px;width:205px;font-size:11.5px;line-height:18px;color:var(--text)}
.review .body b{color:var(--blue);font-weight:400;text-decoration:underline}
.review .who{position:absolute;top:196px;left:27px;font-size:14.5px;font-weight:500}
.review .place{position:absolute;top:217px;left:27px;font-size:12px;color:var(--blue)}
.arrow{position:absolute;top:2962px;width:33px;height:33px;border-radius:50%;border:1px solid #9aa0b4;display:flex;align-items:center;justify-content:center;background:#fff}

/* contact */
.field{position:absolute;border-bottom:1px solid var(--line);font-size:12px;color:var(--muted);padding-bottom:8px}

/* footer */
.footer{position:absolute;left:0;top:3528px;width:1200px;height:313px;background:var(--navy);color:var(--white)}
.footer h4{position:absolute;top:63px;font-size:17px;font-weight:500}
.footer .links{position:absolute;left:377px;top:97px;font-size:12.5px;line-height:27px}
.contact-row{position:absolute;left:541px;display:flex;align-items:center;gap:12px;font-size:12.5px}
.dot-ic{width:26px;height:26px;border-radius:50%;background:var(--blue);display:flex;align-items:center;justify-content:center}
.social{position:absolute;top:175px;width:20px;height:20px;border-radius:50%;border:1.5px solid #fff}
</style>
</head>
<body>

<!-- HERO -->
<section class="hero">
  <div class="deco-ring" style="left:-120px;top:-140px;width:260px;height:340px;border-color:#c5cdf5"></div>
  <div class="deco-ring" style="left:-70px;top:540px;width:140px;height:140px;border-width:26px;border-color:#c5cdf5"></div>
  <div class="deco-ring" style="left:960px;top:-160px;width:360px;height:360px;border-width:30px;border-color:#cfd6f7"></div>
  <div class="logo" style="left:161px;top:26px">Maplecrest<br><span style="font-size:12px;letter-spacing:3px">DENTISTRY</span></div>
  <nav class="nav">
    <a class="active">Home</a><a>About Us</a><a>Services</a><a>Dentists</a><a>Contact Us</a>
  </nav>
  <a class="btn" style="left:877px;top:22px;width:162px;height:41px;font-size:14px">Book Appointment</a>
  <h1>High Quality and<br><span>Painless Dentistry</span></h1>
  <p>If you are in need of high-quality, professional and friendly dental care, look no further than our clinic.</p>
  <a class="btn" style="left:161px;top:408px;width:161px;height:41px;font-size:13.5px">Learn More</a>
</section>
<div class="hero-photo" role="img" aria-label="Smiling dentist in a white coat with arms crossed, a blue leaf shape, a tooth model and dental mirror"></div>
<div class="info-card" style="left:912px;top:330px;width:249px;height:86px;background:var(--blue);color:#fff;padding-left:22px">
  <svg width="42" height="42" viewBox="0 0 42 42"><circle cx="21" cy="21" r="18" fill="none" stroke="#fff" stroke-width="2.5"/><path d="M21 11v11l7 4" fill="none" stroke="#fff" stroke-width="2.5" stroke-linecap="round"/></svg>
  <div><div class="t1">Opening Hours</div><div class="t2">Mon to Sat 08:00 - 20:00</div></div>
</div>
<div class="info-card" style="left:626px;top:502px;width:248px;height:87px;background:#fff;padding-left:22px">
  <svg width="40" height="40" viewBox="0 0 24 24"><path fill="#3e5dd8" d="M6.6 10.8c1.4 2.8 3.8 5.1 6.6 6.6l2.2-2.2c.3-.3.7-.4 1-.2 1.1.4 2.3.6 3.6.6.6 0 1 .4 1 1V20c0 .6-.4 1-1 1C10.6 21 3 13.4 3 4c0-.6.4-1 1-1h3.5c.6 0 1 .4 1 1 0 1.3.2 2.5.6 3.6.1.3 0 .7-.2 1L6.6 10.8z"/></svg>
  <div><div class="t1">Need Dental Services?</div><div class="t2" style="color:var(--text)">Call: +1 555 210 4477</div></div>
</div>

<!-- ABOUT -->
<div class="ph" role="img" aria-label="Decorative leaf-shaped collage of dental photos" style="left:161px;top:771px;width:205px;height:172px;border-radius:50% 50% 40% 40%;background:linear-gradient(135deg,#c9d0f3,#7c8fd6 60%,#dfe4f5)"></div>
<div class="ph" role="img" aria-label="Two smiling dentists in scrubs giving an okay gesture" style="left:161px;top:970px;width:213px;height:212px;background:linear-gradient(180deg,#e8ecf3,#6b86b9 55%,#1f3565)"></div>
<div class="ph" role="img" aria-label="Patient smiling in the chair during a dental exam" style="left:386px;top:833px;width:213px;height:312px;background:linear-gradient(160deg,#5f6a78,#c9a89a 45%,#3f67b5 85%)"></div>
<div class="abs eyebrow" style="left:662px;top:803px">About Us</div>
<h2 class="abs section-title" style="left:661px;top:830px;width:400px;line-height:38px">Professionals and Personalized Dental Excellence</h2>
<p class="abs lead" style="left:662px;top:953px;width:378px;font-size:14px">Welcome to our YourlogoChapters dedicated to empowering pet owners with valuable knowledge and resources.</p>
<p class="abs lead" style="left:662px;top:1024px;width:378px;font-size:14px">Welcome to our YourlogoChapters dedicated to empowering pet owners with valuable knowledge and resources.</p>
<a class="btn" style="left:662px;top:1108px;width:161px;height:41px">Learn More</a>

<!-- SERVICES -->
<section class="services"></section>
<div class="abs eyebrow center" style="top:1328px">Our Services</div>
<h2 class="abs section-title center" style="top:1355px">Complete Care for Every Smile</h2>
<p class="abs lead center" style="top:1403px">Welcome to our YourlogoChapters dedicated to empowering pet owners with<br>valuable knowledge and resources.</p>

<div class="svc" style="left:54px">
  <div class="icon"><svg width="30" height="30" viewBox="0 0 24 24"><path d="M7 3c-2.5 0-4 2-4 4.5 0 3 1.5 4.5 2 7.5.4 2.6 1 6 2.5 6s1.8-5 4.5-5 3 5 4.5 5 2.1-3.4 2.5-6c.5-3 2-4.5 2-7.5C21 5 19.5 3 17 3c-2 0-3 1-5 1S9 3 7 3z" fill="none" stroke="#3e5dd8" stroke-width="1.4"/></svg></div>
  <h3>Cosmetic Dentistry</h3>
  <p>It is a long established fact that a reader will be distracted by when looking at its layout.</p>
  <a class="more">LEARN MORE</a>
  <div class="thumb" role="img" aria-label="Close-up of white teeth and gums"></div>
</div>
<div class="svc" style="left:331px">
  <div class="icon"><svg width="30" height="30" viewBox="0 0 24 24"><path d="M7 3h10c1.5 0 2 1.2 2 2.5S17.5 9 12 9 5 7 5 5.5 5.5 3 7 3zM9 11h6M9.5 13.5h5M10 16h4M11 18.5h2M12 9v12" fill="none" stroke="#3e5dd8" stroke-width="1.4" stroke-linecap="round"/></svg></div>
  <h3>Implants</h3>
  <p>It is a long established fact that a reader will be distracted by when looking at its layout.</p>
  <a class="more">LEARN MORE</a>
  <div class="thumb" role="img" aria-label="Dental implant model between teeth"></div>
</div>
<div class="svc" style="left:608px">
  <div class="icon"><svg width="30" height="30" viewBox="0 0 24 24"><path d="M4 4v10M4 4h3v5H4M12 6c-1.5 0-3 1.2-3 3.5 0 2.5 1 3.5 1.5 6 .3 1.8.7 4 1.8 4s1.2-3 2.7-3 1.7 3 2.7 3 1.5-2.2 1.8-4c.5-2.5 1.5-3.5 1.5-6C21 7.2 19.5 6 18 6c-1.5 0-2 .8-3 .8S13.5 6 12 6z" fill="none" stroke="#3e5dd8" stroke-width="1.4" stroke-linecap="round"/></svg></div>
  <h3>Dental Hygiene</h3>
  <p>It is a long established fact that a reader will be distracted by when looking at its layout.</p>
  <a class="more">LEARN MORE</a>
  <div class="thumb" role="img" aria-label="Clean molars on pink gums"></div>
</div>
<div class="svc" style="left:885px">
  <div class="icon"><svg width="30" height="30" viewBox="0 0 24 24"><rect x="3" y="6" width="18" height="12" rx="4" fill="none" stroke="#3e5dd8" stroke-width="1.4"/><path d="M3 12h18M7.5 6v12M12 6v12M16.5 6v12" stroke="#3e5dd8" stroke-width="1.2"/></svg></div>
  <h3>Emergency Services</h3>
  <p>It is a long established fact that a reader will be distracted by when looking at its layout.</p>
  <a class="more">LEARN MORE</a>
  <div class="thumb" role="img" aria-label="Tooth with red inflamed area"></div>
</div>

<svg class="abs" style="left:580px;top:1776px" width="40" height="20" viewBox="0 0 40 20"><circle cx="5" cy="10" r="3" fill="#3e5dd8"/><circle cx="20" cy="10" r="7" fill="none" stroke="#3e5dd8" stroke-width="1.5"/><circle cx="20" cy="10" r="3.5" fill="#3e5dd8"/><circle cx="35" cy="10" r="3" fill="#3e5dd8"/></svg>
<a class="btn" style="left:520px;top:1819px;width:160px;height:40px">View All Services</a>

<!-- TEAM -->
<div class="abs eyebrow center" style="top:1965px">Meet Our Dental Team</div>
<h2 class="abs section-title center" style="top:1991px">Committed to Your Smile</h2>
<p class="abs lead center" style="top:2040px">Welcome to our YourlogoChapters dedicated to empowering pet owners with<br>valuable knowledge and resources.</p>

<div class="member" style="left:161px;background:linear-gradient(180deg,#dfe5ef,#4f86d4 70%)" role="img" aria-label="Dentist in blue scrubs holding dental tools">
  <div class="tag"><div class="name">Dr. Clara Whitfield</div><div class="role">Lead Dentist</div></div></div>
<div class="member" style="left:386px;background:linear-gradient(180deg,#8a8f97,#c9ccd3 55%,#eef0f4)" role="img" aria-label="Dentist in white coat giving thumbs up">
  <div class="tag"><div class="name">Dr. Clara Whitfield</div><div class="role">Lead Dentist</div></div></div>
<div class="member" style="left:611px;background:linear-gradient(180deg,#55c6d9,#2fa9c4 60%,#3d7fd0)" role="img" aria-label="Dentist with glasses holding dental mirror">
  <div class="tag"><div class="name">Dr. Clara Whitfield</div><div class="role">Lead Dentist</div></div></div>
<div class="member" style="left:836px;background:linear-gradient(180deg,#cdd2da,#e9ecf1 50%,#b8c0cc)" role="img" aria-label="Dentist in white coat in clinic">
  <div class="tag"><div class="name">Dr. Clara Whitfield</div><div class="role">Lead Dentist</div></div></div>
<a class="btn" style="left:520px;top:2406px;width:160px;height:40px">View All Team</a>

<!-- TESTIMONIALS -->
<div class="abs eyebrow center" style="top:2503px">Our Testimonial</div>
<h2 class="abs section-title center" style="top:2530px">Pleasing Patients Is Our Greatest Achievement</h2>
<p class="abs lead center" style="top:2578px">Welcome to our YourlogoChapters dedicated to empowering pet owners with<br>valuable knowledge and resources.</p>

<svg width="0" height="0" style="position:absolute"><defs><symbol id="star" viewBox="0 0 24 24"><path fill="#3e5dd8" d="M12 2l2.9 6.9 7.1.6-5.4 4.7 1.6 7L12 17.5 5.8 21.2l1.6-7L2 9.5l7.1-.6z"/></symbol></defs></svg>

<div class="review faded" style="left:-64px">
  <div class="stars"><svg width="18" height="18"><use href="#star"/></svg><svg width="18" height="18"><use href="#star"/></svg><svg width="18" height="18"><use href="#star"/></svg><svg width="18" height="18"><use href="#star"/></svg><svg width="18" height="18"><use href="#star"/></svg></div>
  <div class="quote">“This Whole Practice<br>Is Wonderful!!”</div>
  <div class="body">It is a long established fact that a reader will be distracted by the of using Lorem Ipsum. <b>READ MORE</b></div>
  <div class="who">Nora P.</div><div class="place">Elm Hollow</div>
</div>
<div class="review" style="left:204px">
  <div class="stars"><svg width="18" height="18"><use href="#star"/></svg><svg width="18" height="18"><use href="#star"/></svg><svg width="18" height="18"><use href="#star"/></svg><svg width="18" height="18"><use href="#star"/></svg><svg width="18" height="18"><use href="#star"/></svg></div>
  <div class="quote">“This Whole Practice<br>&nbsp;Is Wonderful!!”</div>
  <div class="body">It is a long established fact that a reader will be distracted by the of using Lorem Ipsum. <b>READ MORE</b></div>
  <div class="who">Nora P.</div><div class="place">Elm Hollow</div>
</div>
<div class="review" style="left:472px">
  <div class="stars"><svg width="18" height="18"><use href="#star"/></svg><svg width="18" height="18"><use href="#star"/></svg><svg width="18" height="18"><use href="#star"/></svg><svg width="18" height="18"><use href="#star"/></svg><svg width="18" height="18"><use href="#star"/></svg></div>
  <div class="quote">“This Whole Practice<br>&nbsp;Is Wonderful!!”</div>
  <div class="body">It is a long established fact that a reader will be distracted by the of using Lorem Ipsum. <b>READ MORE</b></div>
  <div class="who">Nora P.</div><div class="place">Elm Hollow</div>
</div>
<div class="review" style="left:741px">
  <div class="stars"><svg width="18" height="18"><use href="#star"/></svg><svg width="18" height="18"><use href="#star"/></svg><svg width="18" height="18"><use href="#star"/></svg><svg width="18" height="18"><use href="#star"/></svg><svg width="18" height="18"><use href="#star"/></svg></div>
  <div class="quote">“This Whole Practice<br>&nbsp;Is Wonderful!!”</div>
  <div class="body">It is a long established fact that a reader will be distracted by the of using Lorem Ipsum. <b>READ MORE</b></div>
  <div class="who">Nora P.</div><div class="place">Elm Hollow</div>
</div>
<div class="review faded" style="left:1010px">
  <div class="stars"><svg width="18" height="18"><use href="#star"/></svg><svg width="18" height="18"><use href="#star"/></svg><svg width="18" height="18"><use href="#star"/></svg><svg width="18" height="18"><use href="#star"/></svg><svg width="18" height="18"><use href="#star"/></svg></div>
  <div class="quote">“This Whole Practice<br>&nbsp;Is Wonderful!!”</div>
  <div class="body">It is a long established fact that a reader will be distracted by the of using Lorem Ipsum. <b>READ MORE</b></div>
  <div class="who">Nora P.</div><div class="place">Elm Hollow</div>
</div>

<div class="arrow" style="left:326px"><svg width="10" height="10" viewBox="0 0 10 10"><path d="M6.5 1.5L3 5l3.5 3.5" fill="none" stroke="#1c1d2b" stroke-width="1.5"/></svg></div>
<div class="arrow" style="left:841px"><svg width="10" height="10" viewBox="0 0 10 10"><path d="M3.5 1.5L7 5 3.5 8.5" fill="none" stroke="#1c1d2b" stroke-width="1.5"/></svg></div>
<div class="abs" style="left:397px;top:2976px;width:406px;height:5px;border-radius:3px;background:#dfe3f0"></div>
<div class="abs" style="left:449px;top:2975px;width:129px;height:7px;border-radius:3px;background:var(--blue)"></div>

<!-- CONTACT -->
<div class="abs" role="img" aria-label="Close-up of a patient receiving dental care with a mirror and gloves" style="left:0;top:3086px;width:359px;height:442px;background:linear-gradient(150deg,#c49a86,#e1c0ae 40%,#9aa0d8 75%,#6d75c4)"></div>
<div class="abs" role="img" aria-label="Blurred dental clinic chair in soft teal and grey" style="left:841px;top:3086px;width:359px;height:442px;background:linear-gradient(160deg,#b9bcc2,#d9dbdf 40%,#8fc4cf 75%,#5aa2b6)"></div>
<div class="abs eyebrow" style="left:359px;width:482px;text-align:center;top:3120px">Contact</div>
<h2 class="abs section-title" style="left:359px;width:482px;text-align:center;top:3143px;font-weight:500">Get In Touch</h2>
<div class="field" style="left:401px;top:3215px;width:177px">Name*</div>
<div class="field" style="left:619px;top:3215px;width:176px">Company Name</div>
<div class="field" style="left:401px;top:3276px;width:177px">Phone</div>
<div class="field" style="left:619px;top:3276px;width:176px">Email Address*</div>
<div class="field" style="left:401px;top:3340px;width:394px;height:73px">Your Message</div>
<a class="btn" style="left:498px;top:3452px;width:204px;height:41px;font-size:13px">SUBMIT</a>

<!-- FOOTER -->
<footer class="footer">
  <div class="logo" style="left:161px;top:107px;color:#fff">Maplecrest<br><span style="font-size:12px;letter-spacing:3px">DENTISTRY</span></div>
  <div class="social" style="left:191px"></div>
  <div class="social" style="left:236px"></div>
  <div class="social" style="left:278px"></div>

  <h4 style="left:377px">Quick Links</h4>
  <div class="links">Home<br>About Us<br>Services<br>Team<br>Contact Us</div>

  <h4 style="left:541px">Contact Us</h4>
  <div class="contact-row" style="top:92px"><span class="dot-ic"><svg width="13" height="13" viewBox="0 0 24 24"><path fill="#fff" d="M6.6 10.8c1.4 2.8 3.8 5.1 6.6 6.6l2.2-2.2c.3-.3.7-.4 1-.2 1.1.4 2.3.6 3.6.6.6 0 1 .4 1 1V20c0 .6-.4 1-1 1C10.6 21 3 13.4 3 4c0-.6.4-1 1-1h3.5c.6 0 1 .4 1 1 0 1.3.2 2.5.6 3.6.1.3 0 .7-.2 1L6.6 10.8z"/></svg></span>+1 555 210 4478</div>
  <div class="contact-row" style="top:133px"><span class="dot-ic"><svg width="13" height="13" viewBox="0 0 24 24"><rect x="3" y="5" width="18" height="14" rx="2" fill="#fff"/><path d="M3 6l9 7 9-7" fill="none" stroke="#3e5dd8" stroke-width="1.8"/></svg></span>hello@maplecrestdental.com</div>
  <div class="contact-row" style="top:172px"><span class="dot-ic"><svg width="13" height="13" viewBox="0 0 24 24"><path fill="#fff" d="M12 2a7 7 0 0 0-7 7c0 5 7 13 7 13s7-8 7-13a7 7 0 0 0-7-7zm0 9.5A2.5 2.5 0 1 1 12 6.5a2.5 2.5 0 0 1 0 5z"/></svg></span>122, Lorem ipsum dolird</div>

  <h4 style="left:790px">Subscribe To Our Newsletter</h4>
  <div class="abs" style="left:790px;top:100px;width:248px;height:35px;background:#fff;font-size:12.5px;color:var(--muted);padding:9px 14px">E-mail</div>
  <a class="btn" style="left:790px;top:145px;width:101px;height:34px;font-size:13px;border-radius:0">SUBSCRIBE</a>

  <div class="abs" style="left:161px;top:258px;width:878px;height:1px;background:#2c3866"></div>
  <div class="abs center" style="top:276px;font-size:12.5px">Copyright © 2025 Maplecrest. All rights reserved.</div>
</footer>

</body>
</html>
```